Book cover design for a collection of poetry - The Lanternfield

Book cover and back design need to be moody, nostalgic, reflective, ethereal. Melancholy and other worldly. Cover design should not be time specific to a period or place but if applicable should reflect British landscape. Book cover should be in tones of blue and must include the title and author (THE LANTERNFIELD BY CORWIN BLACKETT). We love the idea of rain, and looking out of a window. See attached designs. A world you are observing but not in.

Industry/Entity Type

Book Publisher

Font styles to use
Serif
Script

Colors
3176b5
3377b5
85acd3
eaf1f7
0792cd
33a6d7
86cae7
ecf7fb
86cfc6

Requirements
Must have
• The colour blue in it, must be melancholy and reflective.
Nice to have
• Rain in the cover.
Should not have
• Any bright colours.

```html
<!DOCTYPE html>
<html lang="en">
<head>
<meta charset="utf-8">
<title>The Lanternfield – Book Cover Spread</title>
<link rel="stylesheet" href="https://fonts.googleapis.com/css2?family=Sorts+Mill+Goudy&family=Bitter:wght@300;400&display=swap">
<style>
  :root {
    --ink-night: #0c1b22;
    --ink-deep: #102a35;
    --rain-teal: #3f93a8;
    --rain-mist: #86cae7;
    --sky-pale: #dfe7ea;
    --sky-grey: #c5d3d8;
    --mist: #7f9aa3;
    --sea-mid: #5f7c87;
    --sea-dark: #24404c;
    --frame-light: #1d4150;
    --frame-dark: #0e242d;
    --sill: #3c535c;
    --text-light: #eaf1f7;
    --text-soft: #b9c7cc;
  }
  * { margin: 0; padding: 0; box-sizing: border-box; }
  html, body { width: 1200px; height: 895px; overflow: hidden; background: var(--ink-night); }
  .spread {
    position: relative;
    width: 1200px;
    height: 895px;
    background: var(--ink-night);
    overflow: hidden;
  }

  /* Back cover */
  .back-photo {
    position: absolute;
    left: 0; top: 0;
    width: 600px; height: 895px;
    background:
      radial-gradient(ellipse 460px 620px at 110px 170px, rgba(134,202,231,0.9) 0%, rgba(63,147,168,0.8) 38%, rgba(16,42,53,0.65) 78%, rgba(12,27,34,0) 100%),
      linear-gradient(90deg, #143642 0%, var(--ink-night) 100%);
  }
  .back-photo::after {
    content: "";
    position: absolute; inset: 0;
    background: linear-gradient(90deg, rgba(12,27,34,0) 55%, var(--ink-night) 100%);
  }
  .blurb {
    position: absolute;
    left: 286px; top: 174px;
    transform: translateX(-50%);
    text-align: center;
    font-family: "Sorts Mill Goudy", Georgia, serif;
    font-size: 16.5px;
    line-height: 37.4px;
    letter-spacing: 0.5px;
    color: var(--text-light);
    white-space: nowrap;
  }
  .blurb .book-name { font-weight: 700; }

  /* Spine */
  .spine {
    position: absolute;
    left: 561px; top: 0;
    width: 76px; height: 895px;
  }
  .spine-text {
    position: absolute;
    left: 50%; top: 104px;
    width: 700px;
    transform-origin: 0 0;
    transform: rotate(90deg) translateY(-50%);
    display: flex;
    align-items: baseline;
    white-space: nowrap;
    color: var(--text-light);
  }
  .spine-title {
    font-family: "Bitter", Georgia, serif;
    font-weight: 300;
    font-size: 27px;
    letter-spacing: 5px;
  }
  .spine-author {
    margin-left: 96px;
    font-family: "Sorts Mill Goudy", Georgia, serif;
    font-size: 25px;
    letter-spacing: 0.5px;
    color: var(--text-soft);
  }

  /* Front cover */
  .front-photo {
    position: absolute;
    left: 637px; top: 0;
    width: 563px; height: 895px;
    background: linear-gradient(180deg,
      var(--sky-pale) 0%, var(--sky-grey) 30%, #aebfc5 34%, var(--mist) 40%,
      var(--sea-mid) 58%, #3b5763 60%, var(--sea-dark) 82%,
      var(--sill) 86%, #22323a 91%, #111619 100%);
  }
  .window-frame {
    position: absolute;
    left: 637px; top: 0;
    width: 563px; height: 895px;
  }
  .front-shade {
    position: absolute;
    left: 637px; top: 0;
    width: 563px; height: 895px;
    background: linear-gradient(90deg, var(--ink-night) 0%, rgba(12,27,34,0) 10%);
  }
  .front-title {
    position: absolute;
    right: 94px; top: 364px;
    text-align: right;
    color: var(--text-light);
  }
  .front-title .title {
    font-family: "Bitter", Georgia, serif;
    font-weight: 400;
    font-size: 29px;
    letter-spacing: 1px;
    line-height: 1.1;
  }
  .front-title .author {
    font-family: "Bitter", Georgia, serif;
    font-weight: 300;
    font-size: 19px;
    color: var(--text-soft);
    margin-top: 2px;
    padding-right: 2px;
  }
</style>
</head>
<body>
  <main class="spread">
    <section class="back-cover">
      <div class="back-photo" role="img" aria-label="Rain droplets running down a misted window pane in teal and deep blue"></div>
      <p class="blurb">
        <span class="book-name">The Lanternfield</span> is a collection of poetry<br>
        documenting the lives of an aristocratic couple<br>
        throughout the 20th Century. Told in two parts<br>
        we first meet Charles – aged, crippled and left<br>
        alone in his inherited Marsh House - reflecting<br>
        on his life and his marriage to beautiful Alice<br>
        who we meet in part two. Alice is suicidal,<br>
        manically depressed and struggling with societal<br>
        conventions and life as a wife and mother.<br>
        She meets, harbors and falls in love with a soldier<br>
        during WWII and her world is changed forever.<br>
        Moving through decades, through this life and<br>
        the next - The Lanternfield interweaves themes of<br>
        grief, loss, the after-life, mental illness,<br>
        and ultimately the true nature of love.
      </p>
    </section>

    <section class="spine">
      <div class="spine-text">
        <span class="spine-title">THE LANTERNFIELD</span>
        <span class="spine-author">by Corwin Blackett</span>
      </div>
    </section>

    <section class="front-cover">
      <div class="front-photo" role="img" aria-label="Rain-streaked view of a pale grey sky over misty hills and a dark sea"></div>
      <svg class="window-frame" viewBox="0 0 563 895" aria-hidden="true">
        <defs>
          <linearGradient id="frameTone" x1="0" y1="0" x2="1" y2="0">
            <stop offset="0" stop-color="#0e242d"/>
            <stop offset="0.5" stop-color="#1d4150"/>
            <stop offset="1" stop-color="#10262f"/>
          </linearGradient>
          <linearGradient id="sillTone" x1="0" y1="0" x2="0" y2="1">
            <stop offset="0" stop-color="#4a6570"/>
            <stop offset="1" stop-color="#22323a"/>
          </linearGradient>
        </defs>
        <path fill="url(#frameTone)" fill-rule="evenodd" d="
          M0 0 H537 V772 H0 Z
          M46 0 H191 V50 H46 Z  M204 0 H349 V50 H204 Z  M362 0 H494 V50 H362 Z
          M46 63 H191 V280 H46 Z  M204 63 H349 V280 H204 Z  M362 63 H494 V280 H362 Z
          M49 307 H191 V519 H49 Z  M208 307 H349 V519 H208 Z  M365 307 H494 V519 H365 Z
          M49 528 H191 V740 H49 Z  M208 528 H349 V740 H208 Z  M365 528 H494 V740 H365 Z"/>
        <rect x="537" y="0" width="26" height="895" fill="#0d1c22"/>
        <rect x="0" y="772" width="563" height="40" fill="url(#sillTone)"/>
        <rect x="0" y="812" width="563" height="83" fill="#111619"/>
      </svg>
      <div class="front-shade"></div>
      <div class="front-title">
        <h1 class="title">THE LANTERNFIELD</h1>
        <p class="author">by Corwin Blackett</p>
      </div>
    </section>
  </main>
</body>
</html>
```